Business Card Design Project

Corwen Property Management

Our Business is residential property management, we therefore need a card that displays a professional image, but is clear and concise, and easy to read
Updates

We are committed now guys and girls, loving what we are seeing so far! 

Target Market(s)

Landlords, Rental Property Owners

Industry/Entity Type

Residential

Requirements
Must have
• Dean Fosterly - Principal
Tessa Fosterly - Director (Property Management)

PO Box 718
Holloway SA 5093

Dean: 0419 372 508
Tessa: 0419 613 947

www.corwenpropertymanagement.com.au
admin@corwenpropertymanagement.com.au

Nice to have
• I would like the card to be double sided, white background on the information side and then colour on the reverse, in blue or black and incorporating our logo

```html
<!DOCTYPE html>
<html lang="en">
<head>
<meta charset="utf-8">
<title>Corwen Property Management – Business Card</title>
<link rel="stylesheet" href="https://fonts.googleapis.com/css2?family=Open+Sans:ital,wght@0,400;0,600;0,700;1,700&display=swap">
<style>
  :root {
    --backdrop: #e8e5e0;
    --card-white: #ffffff;
    --brand-blue: #0d6cb8;
    --name-blue: #1a63ad;
    --detail-blue: #2b86cc;
    --logo-grey: #555759;
    --label-grey: #7a7c7e;
    --number-grey: #6b6d70;
    --web-grey: #333538;
    --bullet-grey: #8a8c8e;
  }
  * { margin: 0; padding: 0; box-sizing: border-box; }
  html, body {
    width: 1200px; height: 750px; overflow: hidden;
    background: var(--backdrop);
    font-family: "Open Sans", Arial, sans-serif;
  }
  .canvas { position: relative; width: 1200px; height: 750px; }

  .card {
    position: absolute; top: 217px; width: 503px; height: 331px;
    box-shadow: 0 2px 8px rgba(0,0,0,0.25);
  }
  .card--front { left: 62px; background: var(--card-white); }
  .card--back {
    left: 637px;
    background: linear-gradient(100deg, #ffffff 0%, #ffffff 28%, #cfe2f1 48%, #5b9fd3 72%, var(--brand-blue) 100%);
  }

  .brand { position: absolute; display: flex; align-items: center; }
  .brand__square { background: var(--brand-blue); flex: none; }
  .brand__name {
    color: var(--logo-grey); font-weight: 700; line-height: 1.05;
  }
  .card--front .brand { left: 30px; top: 20px; gap: 14px; }
  .card--front .brand__square { width: 56px; height: 56px; }
  .card--front .brand__name { font-size: 27px; }

  .card--back .brand { left: 53px; top: 125px; gap: 20px; }
  .card--back .brand__square { width: 80px; height: 80px; }
  .card--back .brand__name { font-size: 38px; }

  .details { position: absolute; left: 16px; top: 106px; }
  .row { position: relative; padding-left: 14px; white-space: nowrap; }
  .row--bullet::before {
    content: ""; position: absolute; left: 0; top: 8px;
    width: 7px; height: 7px; background: var(--bullet-grey);
  }
  .person { font-size: 18px; line-height: 22px; }
  .person__name { color: var(--name-blue); font-weight: 700; font-style: italic; }
  .person__role { color: var(--label-grey); font-weight: 600; font-size: 16px; }
  .person__role small { font-size: 9px; font-weight: 600; }
  .person--second { padding-left: 10px; }

  .address { color: var(--detail-blue); font-weight: 600; font-size: 16px; line-height: 20px; margin-top: 4px; }
  .address--second { padding-left: 14px; }

  .phone { font-size: 16px; line-height: 23px; font-weight: 600; letter-spacing: 0.5px; }
  .phone--first { margin-top: 3px; }
  .phone__label { color: var(--detail-blue); }
  .phone__number { color: var(--number-grey); letter-spacing: 1.2px; }
  .phone--second { padding-left: 14px; }

  .web { position: absolute; left: 16px; top: 262px; color: var(--web-grey); font-size: 15.5px; line-height: 21px; font-weight: 400; }
</style>
</head>
<body>
<main class="canvas">
  <section class="card card--front" aria-label="Card front with contact details">
    <div class="brand">
      <span class="brand__square"></span>
      <span class="brand__name">Corwen<br>Property Management</span>
    </div>
    <div class="details">
      <p class="row row--bullet person"><span class="person__name">Dean Fosterly</span> <span class="person__role">Principal</span></p>
      <p class="row person person--second"><span class="person__name">Tessa Fosterly</span> <span class="person__role">Director <small>(Property Management)</small></span></p>
      <p class="row row--bullet address">PO Box 718</p>
      <p class="row address address--second" style="margin-top:0">Holloway SA 5093</p>
      <p class="row row--bullet phone phone--first"><span class="phone__label">Dean:</span> <span class="phone__number">0419 372 508</span></p>
      <p class="row phone phone--second"><span class="phone__label">Tessa:</span> <span class="phone__number">0419 613 947</span></p>
    </div>
    <div class="web">
      <p>www.corwenpropertymanagement.com.au</p>
      <p>admin@corwenpropertymanagement.com.au</p>
    </div>
  </section>

  <section class="card card--back" aria-label="Card back with brand name">
    <div class="brand">
      <span class="brand__square"></span>
      <span class="brand__name">Corwen<br>Property Management</span>
    </div>
  </section>
</main>
</body>
</html>
```